Infografiken für Unternehmensberatung zu Automatisierung und Digitalisierung
LRPT
Tolle Arbeit in kurzer Zeit fertigestellt. Zügige Kommunikation, Umsetzung und Anpassungen. Ich bin sehr zufrieden und kann Lady Corntwig mit einem gutem Gefühl weiterempfehlen. Danke
Zielgruppe
Unternehmensberatung zu Automatisierung und Digitalisierung
Aufgabenstellung
Hochwertiges und ansprechendes Design der Beratungsprozesse. Grafik soll in verschiedene Größen eingesetzt und farblich auf das CI der Website/Logos abgestimmt sein.
Gerne kann zwischen den drei Kreisen etwas Raum sein oder der äußere Kreis aus einzelnen Feldern bestehen. Die Beschriftung soll an den Kreisradius angepasst werden. Das copyright bitte auch an den Radius des Kreis anpassen.

```html
<!DOCTYPE html>
<html lang="de">
<head>
<meta charset="utf-8">
<title>Beratungsprozess – Zeit &amp; Lebensqualität</title>
<link href="https://fonts.googleapis.com/css2?family=Roboto+Condensed:wght@400;700&display=swap" rel="stylesheet">
<style>
  :root {
    --ring-blue: #bccbdf;
    --navy: #1f4e8f;
    --accent: #1d4f91;
    --beige-light: #fbf6ec;
    --beige-mid: #efe3cc;
    --beige-edge: #d6c19c;
    --beige-text: #7a6450;
    --copyright: #3a3a3a;
    --paper: #ffffff;
  }
  html, body {
    margin: 0;
    width: 1200px;
    height: 1200px;
    overflow: hidden;
    background: var(--paper);
  }
  .process-wheel {
    display: block;
    width: 1200px;
    height: 1200px;
    font-family: "Roboto Condensed", "Arial Narrow", sans-serif;
  }
  .outer-segment { fill: var(--ring-blue); }
  .divider { stroke: var(--paper); stroke-linecap: butt; }
  .divider--outer { stroke-width: 14; }
  .divider--inner { stroke-width: 12; }
  .step-marker { fill: var(--accent); }
  .step-title { fill: var(--navy); font-weight: 700; font-size: 52px; }
  .step-sub { fill: var(--navy); font-weight: 700; font-size: 34px; }
  .step-sub--large { font-size: 44px; }
  .core-title { fill: var(--beige-text); font-weight: 700; font-size: 46px; }
  .core-sub { fill: var(--beige-text); font-weight: 700; font-size: 31px; }
  .hub { fill: var(--accent); stroke: var(--paper); stroke-width: 8; }
  .hub-text { fill: var(--paper); font-weight: 700; font-size: 42px; }
  .copyright { fill: var(--copyright); font-size: 18px; letter-spacing: 0.3px; }
  .copyright-strong { font-weight: 700; }
</style>
</head>
<body>
<svg class="process-wheel" viewBox="0 0 1200 1200" xmlns="http://www.w3.org/2000/svg">
  <defs>
    <radialGradient id="core-fill" cx="600" cy="600" r="322" gradientUnits="userSpaceOnUse">
      <stop offset="0.35" stop-color="var(--beige-light)"/>
      <stop offset="0.7" stop-color="var(--beige-mid)"/>
      <stop offset="1" stop-color="var(--beige-edge)"/>
    </radialGradient>

    <!-- outer ring label paths: clockwise, letters facing outward -->
    <path id="arc-team-title" d="M180 600 A420 420 0 0 1 810 236.3"/>
    <path id="arc-team-sub" d="M225 600 A375 375 0 0 1 787.5 275.25"/>
    <path id="arc-strategy-title" d="M390 236.3 A420 420 0 0 1 1020 600"/>
    <path id="arc-strategy-sub" d="M412.5 275.25 A375 375 0 0 1 975 600"/>
    <path id="arc-audience-title" d="M810 236.3 A420 420 0 0 1 810 963.7"/>
    <path id="arc-audience-sub" d="M787.5 275.25 A375 375 0 0 1 787.5 924.75"/>
    <path id="arc-sales-title" d="M390 963.7 A420 420 0 0 1 390 236.3"/>
    <path id="arc-sales-sub" d="M412.5 924.75 A375 375 0 0 1 412.5 275.25"/>

    <!-- outer ring label paths: counter-clockwise, letters facing inward -->
    <path id="arc-magnet-title" d="M205 600 A395 395 0 0 0 797.5 942.1"/>
    <path id="arc-magnet-sub" d="M155 600 A445 445 0 0 0 822.5 985.4"/>
    <path id="arc-system-title" d="M402.5 942.1 A395 395 0 0 0 995 600"/>
    <path id="arc-system-sub" d="M377.5 985.4 A445 445 0 0 0 1045 600"/>

    <!-- core ring label paths -->
    <path id="arc-auto-title" d="M399.1 484 A232 232 0 0 1 800.9 484"/>
    <path id="arc-auto-sub" d="M433.7 504 A192 192 0 0 1 766.3 504"/>
    <path id="arc-expert-title" d="M426.8 500 A200 200 0 0 0 600 800"/>
    <path id="arc-expert-sub" d="M387.8 477.5 A245 245 0 0 0 600 845"/>
    <path id="arc-scale-sub" d="M600 790 A190 190 0 0 0 764.5 505"/>
    <path id="arc-scale-title" d="M600 845 A245 245 0 0 0 812.2 477.5"/>

    <!-- copyright path -->
    <path id="arc-copyright" d="M70 600 A530 530 0 0 0 865 1059"/>
  </defs>

  <!-- outer ring -->
  <path class="outer-segment" fill-rule="evenodd"
        d="M600 90 A510 510 0 1 1 599.9 90 Z M600 258 A342 342 0 1 0 600.1 258 Z"/>
  <g class="divider divider--outer">
    <line x1="600" y1="600" x2="600" y2="80" transform="rotate(0 600 600)"/>
    <line x1="600" y1="600" x2="600" y2="80" transform="rotate(60 600 600)"/>
    <line x1="600" y1="600" x2="600" y2="80" transform="rotate(120 600 600)"/>
    <line x1="600" y1="600" x2="600" y2="80" transform="rotate(180 600 600)"/>
    <line x1="600" y1="600" x2="600" y2="80" transform="rotate(240 600 600)"/>
    <line x1="600" y1="600" x2="600" y2="80" transform="rotate(300 600 600)"/>
  </g>

  <!-- direction markers -->
  <g class="step-marker">
    <polygon points="1020,610 1080,610 1050,642" transform="rotate(-90 600 600)"/>
    <polygon points="1020,610 1080,610 1050,642" transform="rotate(-30 600 600)"/>
    <polygon points="1010,610 1070,610 1040,642" transform="rotate(30 600 600)"/>
    <polygon points="990,610 1050,610 1020,642" transform="rotate(90 600 600)"/>
    <polygon points="1010,610 1070,610 1040,642" transform="rotate(150 600 600)"/>
    <polygon points="1020,610 1080,610 1050,642" transform="rotate(210 600 600)"/>
  </g>

  <!-- outer ring labels -->
  <text class="step-title"><textPath href="#arc-team-title" startOffset="50%" text-anchor="middle">Team bilden</textPath></text>
  <text class="step-sub"><textPath href="#arc-team-sub" startOffset="50%" text-anchor="middle">&amp; entwickeln</textPath></text>

  <text class="step-title"><textPath href="#arc-strategy-title" startOffset="50%" text-anchor="middle">Strategisch</textPath></text>
  <text class="step-sub"><textPath href="#arc-strategy-sub" startOffset="50%" text-anchor="middle">planen</textPath></text>

  <text class="step-title"><textPath href="#arc-audience-title" startOffset="50%" text-anchor="middle">Eindeutige</textPath></text>
  <text class="step-sub"><textPath href="#arc-audience-sub" startOffset="50%" text-anchor="middle">Zielgruppe</textPath></text>

  <text class="step-title"><textPath href="#arc-system-title" startOffset="50%" text-anchor="middle">Systematisch</textPath></text>
  <text class="step-sub"><textPath href="#arc-system-sub" startOffset="50%" text-anchor="middle">informieren</textPath></text>

  <text class="step-title"><textPath href="#arc-magnet-title" startOffset="50%" text-anchor="middle">Magnet-</textPath></text>
  <text class="step-sub step-sub--large"><textPath href="#arc-magnet-sub" startOffset="50%" text-anchor="middle">Marketing</textPath></text>

  <text class="step-title"><textPath href="#arc-sales-title" startOffset="50%" text-anchor="middle">Verkaufen</textPath></text>
  <text class="step-sub"><textPath href="#arc-sales-sub" startOffset="50%" text-anchor="middle">&amp; betreuen</textPath></text>

  <!-- core ring -->
  <circle cx="600" cy="600" r="322" fill="url(#core-fill)"/>
  <g class="divider divider--inner">
    <line x1="600" y1="600" x2="600" y2="270" transform="rotate(60 600 600)"/>
    <line x1="600" y1="600" x2="600" y2="270" transform="rotate(180 600 600)"/>
    <line x1="600" y1="600" x2="600" y2="270" transform="rotate(300 600 600)"/>
  </g>

  <text class="core-title"><textPath href="#arc-auto-title" startOffset="50%" text-anchor="middle">Automatisieren</textPath></text>
  <text class="core-sub"><textPath href="#arc-auto-sub" startOffset="50%" text-anchor="middle">&amp; Digitalisieren</textPath></text>

  <text class="core-title"><textPath href="#arc-expert-title" startOffset="50%" text-anchor="middle">Experten</textPath></text>
  <text class="core-sub"><textPath href="#arc-expert-sub" startOffset="50%" text-anchor="middle">Positionierung</textPath></text>

  <text class="core-sub"><textPath href="#arc-scale-sub" startOffset="50%" text-anchor="middle">Skalierbares</textPath></text>
  <text class="core-title"><textPath href="#arc-scale-title" startOffset="50%" text-anchor="middle">Unternehmen</textPath></text>

  <!-- hub -->
  <circle class="hub" cx="600" cy="600" r="127"/>
  <text class="hub-text" text-anchor="middle">
    <tspan x="600" y="540">Zeit &amp;</tspan>
    <tspan x="600" y="588">Lebens-</tspan>
    <tspan x="600" y="636">qualität</tspan>
  </text>

  <!-- copyright -->
  <text class="copyright"><textPath href="#arc-copyright" startOffset="48%" text-anchor="middle">Copyright © <tspan class="copyright-strong">Gleichklang Beratung KG</tspan> | www.gleichklang-beratung.de</textPath></text>
</svg>
</body>
</html>
```